Landing page in the senior sector

We need a landing page for families looking for retirement homes for their parent. The target is rather old (50-60 years old). The mandatory fields are Name, Email, Phone. The optional fields are budget, research zipcode, Emergency (,,). It is important to note that this is a free service that we offer to families in research. It should be noted that they are often in distress and repulsive. Need a mobile landing We need a landing page to recruit families looking for retirement homes for their parent. The target is rather old (50-60 years old). Required fields are Name, Email, Phone. The optional fields (they may not appear at all) are Budget, Search CP, Emergency (,,). It is important to mention that this is a free service that we offer to families in search. It should be noted that they are often in distress and that asking them for input may let tel may seem repulsive. Also need a mobile version

Target Market(s)

rather old (50-60 years old) / rather old (50-60 years old)

Coding

Coded - Design and coding required

Number of Pages Required

2 page

Font styles to use
Sans Serif

Colors

Designer to choose colors to be used in the design.

Requirements
Must have
• - A form with the 3 mandatory fields / A form with the 3 mandatory fields - Optimized for conversion / Optimized for conversion

```html
<!DOCTYPE html>
<html lang="en">
<head>
<meta charset="UTF-8">
<title>Evergreen Haven – Certified Care for your Family</title>
<link href="https://fonts.googleapis.com/css2?family=Roboto:wght@400;500;700&family=Playfair+Display:wght@700&display=swap" rel="stylesheet">
<style>
  :root {
    --page-bg: #ffffff;
    --card-bg: #ffffff;
    --ink-dark: #1d3350;
    --ink-muted: #555b61;
    --brand-blue: #1565a8;
    --band-top: #0b78c8;
    --band-bottom: #0a4f8f;
    --brand-green: #a6cb26;
    --field-border: #d3d6d9;
    --required: #e32020;
    --white: #ffffff;
  }
  * { box-sizing: border-box; margin: 0; padding: 0; }
  html, body {
    width: 1200px; height: 1200px; overflow: hidden;
    background: var(--page-bg);
    font-family: "Roboto", Arial, sans-serif;
  }
  .landing {
    position: absolute; left: 262px; top: 132px;
    width: 676px; height: 932px;
    background: var(--card-bg);
    box-shadow: 0 0 6px rgba(0,0,0,0.12);
    overflow: hidden;
  }
  .hero {
    position: absolute; left: 0; top: 0; width: 100%; height: 484px;
  }
  .hero-photo {
    position: absolute; inset: 0;
    background:
      linear-gradient(180deg, rgba(0,0,0,0) 45%, rgba(10,40,60,0.55) 100%),
      linear-gradient(115deg, #eef0c8 0%, #c9d98a 30%, #7fa56a 55%, #4f8a7c 75%, #b8d22e 100%);
  }
  .brand {
    position: absolute; left: 52px; top: 58px;
    display: flex; align-items: center; gap: 6px;
    font-size: 14px; font-weight: 700; color: var(--brand-blue);
    letter-spacing: 0.2px;
  }
  .brand-mark {
    width: 12px; height: 12px; background: var(--brand-blue);
  }
  .hotline {
    position: absolute; right: 49px; top: 34px;
    display: flex; align-items: center; gap: 10px;
    font-size: 24px; font-weight: 500; color: var(--ink-dark);
    letter-spacing: 1px;
  }
  .hotline-icon {
    width: 29px; height: 29px; border-radius: 50%;
    background: var(--ink-dark);
    display: flex; align-items: center; justify-content: center;
  }
  .hero-copy {
    position: absolute; left: 0; right: 0; top: 240px;
    text-align: center; color: var(--white);
  }
  .hero-kicker {
    font-size: 21px; font-weight: 700; letter-spacing: 0.3px;
    text-shadow: 0 1px 3px rgba(0,0,0,0.35);
  }
  .hero-title {
    margin-top: 8px;
    font-family: "Playfair Display", Georgia, serif;
    font-size: 51px; font-weight: 700; line-height: 56px;
    letter-spacing: 1px;
    text-shadow: 0 2px 4px rgba(0,0,0,0.35);
  }
  .offer-band {
    position: absolute; left: 0; top: 484px; width: 100%; height: 89px;
    background: linear-gradient(180deg, var(--band-top), var(--band-bottom));
    color: var(--white); text-align: center;
    padding-top: 17px;
  }
  .offer-question { font-size: 19px; font-weight: 400; }
  .offer-cta { margin-top: 6px; font-size: 26px; font-weight: 700; letter-spacing: 2px; }
  .reserve-form {
    position: absolute; left: 128px; top: 612px; width: 420px;
  }
  .field { position: relative; margin-bottom: 18px; }
  .field::after {
    content: "*"; position: absolute; right: 8px; top: -10px;
    color: var(--required); font-size: 10px;
  }
  .field input {
    width: 100%; height: 49px;
    border: 2px solid var(--field-border); border-radius: 2px;
    padding: 0 18px;
    font-family: "Roboto", Arial, sans-serif; font-size: 13px;
    color: var(--ink-muted); background: var(--white);
  }
  .field input::placeholder { color: var(--ink-muted); }
  .form-note {
    margin-top: -4px; padding-left: 5px;
    font-size: 11px; color: var(--ink-muted);
  }
  .form-note span { color: var(--required); }
  .reserve-button {
    display: block; margin-top: 28px; width: 419px; height: 47px;
    border: none; background: var(--brand-green); color: var(--white);
    font-family: "Roboto", Arial, sans-serif; font-size: 17px; font-weight: 700;
    letter-spacing: 0.5px;
  }
</style>
</head>
<body>
  <main class="landing">
    <section class="hero">
      <div class="hero-photo" role="img" aria-label="Photo of an elderly couple walking hand in hand outdoors, seen from behind, tinted green and yellow"></div>
      <div class="brand"><span class="brand-mark"></span>Evergreen Haven</div>
      <div class="hotline">
        <span class="hotline-icon">
          <svg width="12" height="17" viewBox="0 0 12 17" aria-hidden="true">
            <rect x="1" y="1" width="10" height="15" rx="2" fill="none" stroke="#ffffff" stroke-width="1.4"/>
            <line x1="4.5" y1="13" x2="7.5" y2="13" stroke="#ffffff" stroke-width="1.2"/>
          </svg>
        </span>
        555-014-2290
      </div>
      <div class="hero-copy">
        <p class="hero-kicker">WE CAN HELP YOU TODAY</p>
        <h1 class="hero-title">Certified Care<br>for your Family</h1>
      </div>
    </section>
    <section class="offer-band">
      <p class="offer-question">Looking for assisted Living Home?</p>
      <p class="offer-cta">Reserve yours Today!</p>
    </section>
    <form class="reserve-form">
      <div class="field"><input type="text" placeholder="Enter your name"></div>
      <div class="field"><input type="email" placeholder="Enter your email"></div>
      <div class="field"><input type="tel" placeholder="Enter your phone"></div>
      <p class="form-note"><span>*</span> marks are mandatory fields</p>
      <button type="button" class="reserve-button">RESERVE TODAY!</button>
    </form>
  </main>
</body>
</html>
```